Twitter Bootstrap Website Design (Gaming Themed)

I need a website designed using Twitter Bootstrap for a Rewards website. We'd like to see a gaming based design as the site will cater mostly to gamers.
This is a rewards site similar to sites like LootPenny
I only need the HTML/CSS design.
I need these pages:
1. Homepage for non-logged in users which will also have a sign up form
2. Homepage for logged in users
3. Profile Page
4. Rewards page which will display items that the user can redeem
a) A drop-down to sort by item category
5. Rewards page item details which will display a single item's details
6. About, FAQ, Terms Of Service Pages
Target Market(s)
13 to 30 year old gamers
Mostly males
Industry/Entity Type
It Service
Look and feel

```html
<!DOCTYPE html>
<html lang="en">
<head>
<meta charset="utf-8">
<title>Sitename Rewards</title>
<link rel="stylesheet" href="https://fonts.googleapis.com/css2?family=Russo+One&family=Lato:wght@300;400;700&family=Open+Sans:wght@600;700&display=swap">
<style>
  :root {
    --bar-dark: #555555;
    --bar-light: #dcdcdc;
    --text-dark: #4f4f4f;
    --text-muted: #8a8a8a;
    --white: #ffffff;
    --social-blue: #3b5998;
    --input-border: #c9d6df;
    --cta-grey: #d9d9d9;
    --footer-grey: #d8d8d8;
    --amount-grey: #777777;
    --wall-cream: #efe6da;
    --shelf-wood: #d9b48e;
    --hair-brown: #8a5a3a;
    --sofa-green: #9aa85a;
    --shirt-blue: #8fb3d9;
    --wall-light: #f1ece8;
    --table-wood: #d4a57a;
  }
  * { box-sizing: border-box; margin: 0; padding: 0; }
  html, body { width: 1200px; height: 882px; overflow: hidden; background: var(--white); }
  .page { position: relative; width: 1200px; height: 882px; font-family: "Lato", sans-serif; }

  .topbar { position: absolute; left: 0; top: 0; width: 1200px; height: 71px; background: var(--bar-dark); }
  .brand { position: absolute; left: 27px; top: 17px; font-family: "Russo One", sans-serif; font-size: 28px; letter-spacing: 3px; color: #e8e8e8; }
  .tab { position: absolute; top: 11px; height: 60px; font-family: "Russo One", sans-serif; font-size: 16px; display: flex; align-items: center; justify-content: center; }
  .tab-plain { left: 930px; width: 110px; color: #f0f0f0; }
  .tab-active { left: 1041px; width: 127px; background: var(--white); color: var(--text-dark); border-radius: 8px 8px 0 0; }

  .mainnav { position: absolute; left: 0; top: 71px; width: 1200px; height: 29px; background: var(--bar-light); }
  .mainnav a { position: absolute; top: 6px; font-family: "Russo One", sans-serif; font-size: 14px; letter-spacing: 1px; color: var(--text-dark); text-decoration: none; }

  .hero-photo { position: absolute; left: 0; top: 100px; width: 1200px; height: 649px;
    background:
      linear-gradient(180deg, rgba(239,230,218,0) 55%, rgba(154,168,90,0.55) 80%, rgba(154,168,90,0.35) 100%),
      linear-gradient(90deg, var(--wall-cream) 0%, var(--hair-brown) 12%, var(--shelf-wood) 24%, var(--sofa-green) 34%, var(--shirt-blue) 48%, var(--shirt-blue) 58%, var(--wall-light) 72%, var(--table-wood) 100%); }

  .signup { position: absolute; left: 716px; top: 71px; width: 452px; height: 469px; background: var(--white); border-radius: 0 0 8px 8px; }
  .social-btn { position: absolute; left: 41px; top: 29px; width: 379px; height: 54px; background: var(--social-blue); border-radius: 2px; color: var(--white); font-weight: 700; font-size: 22px; display: flex; align-items: center; justify-content: center; padding-left: 30px; }
  .social-btn .mark { position: absolute; left: 12px; top: 12px; width: 30px; height: 30px; background: var(--white); border-radius: 2px; }
  .divider { position: absolute; left: 41px; top: 96px; width: 379px; display: flex; align-items: center; gap: 8px; font-size: 15px; font-weight: 300; color: var(--text-muted); }
  .divider::before, .divider::after { content: ""; flex: 1; height: 1px; background: var(--input-border); }
  .field { position: absolute; left: 41px; width: 379px; height: 51px; border: 1px solid var(--input-border); border-radius: 3px; padding-left: 26px; display: flex; align-items: center; font-size: 16px; color: var(--text-muted); }
  .legal { position: absolute; left: 45px; top: 331px; width: 370px; font-family: Arial, sans-serif; font-size: 11px; line-height: 14px; color: #555; }
  .cta { position: absolute; left: 41px; top: 397px; width: 382px; height: 49px; background: var(--cta-grey); font-family: "Open Sans", sans-serif; font-weight: 700; font-size: 23px; color: var(--text-dark); display: flex; align-items: center; justify-content: center; }

  .tagline { position: absolute; left: 0; top: 749px; width: 1200px; height: 32px; background: var(--bar-dark); font-family: "Russo One", sans-serif; font-size: 16px; letter-spacing: 2px; color: #d6d6d6; display: flex; align-items: center; justify-content: center; }
  .totals { position: absolute; left: 0; top: 781px; width: 1200px; height: 101px; background: var(--footer-grey); font-family: "Open Sans", sans-serif; font-weight: 700; font-size: 45px; color: var(--text-dark); display: flex; align-items: center; justify-content: center; gap: 14px; }
  .totals .amount { font-size: 57px; color: var(--amount-grey); }
</style>
</head>
<body>
<div class="page">
  <header class="topbar">
    <div class="brand">SITENAME REWARDS</div>
    <div class="tab tab-plain">SIGN UP</div>
    <div class="tab tab-active">SIGN UP</div>
  </header>

  <nav class="mainnav">
    <a style="left:27px">HOME</a>
    <a style="left:154px">ABOUT US</a>
    <a style="left:318px">FAQ</a>
    <a style="left:433px">TERMS OF USE</a>
  </nav>

  <div class="hero-photo" role="img" aria-label="Photo of two excited young gamers holding game controllers on a green sofa in a bright living room, a bowl of chips on the wooden table"></div>

  <section class="signup">
    <div class="social-btn"><span class="mark"></span>Sign Up with FriendHub</div>
    <div class="divider">or sign up with your email below</div>
    <div class="field" style="top:133px">Email Address</div>
    <div class="field" style="top:196px">Password</div>
    <div class="field" style="top:258px">Confirm Password</div>
    <p class="legal">By Signing up I agree to the Terms and Privacy Policy. I also agree to receive periodic emails with offers and promotional marketing messages from Sitename</p>
    <div class="cta">Free. Get started</div>
  </section>

  <div class="tagline">START EARNING FREE GIFT CARDS TODAY</div>
  <div class="totals"><span>Already has</span><span class="amount">$48,324,509</span><span>in Rewards</span></div>
</div>
</body>
</html>
```